Real Estate Seller Financing Postcard

I need a postcard that lays out these options contained in the notes that grabs attention, explains the two options easily and is eye-catching. The front needs to have the percentages on it and information about it and on the other side One side exact Text is:
"Monthly income without tenant headaches" in big letters. Also on front "Get
110%
add an "or"
160% of market value for your property. ". The percentages should be displayed and that is not to be a sentence of text. Other side text: I need bullets points for these "Formal protection as a lien holder against home
No commission or closing cost
Fast closings possible
Property taken as is so no repairs.

Add to the top of the back in "It’s simple. I am a new investor without down payment capital who still want to double our portfolio this year to grow our portfolio."
Here are the two options that are to be the largest part of the back
Option 1, you can receive 80% now cash and 30% over a short period of time including interest.

Option 2, where act like a bank allowing you to make 150% if you finance the whole property(ies). No gimmicks and surprises, just simple unconventional financing.

Include Logo Somewhere

Target Market(s)

Property Owners Wanting to Sell Their Property

Industry/Entity Type

Real Estate Investing

Requirements
Must have
• The options promiment and each side with its respective information. Must have logo somewhere
Nice to have
• The options in color other than black.
Should not have
• A picture of money on the front. Any other image is okay.

```html
<!DOCTYPE html>
<html lang="en">
<head>
<meta charset="utf-8">
<title>Halden Real Estate Group – Seller Financing Postcard</title>
<link href="https://fonts.googleapis.com/css2?family=Montserrat:wght@300;400;500;600;800;900&display=swap" rel="stylesheet">
<style>
  :root{
    --backdrop:#636466;
    --navy:#1b4594;
    --azure:#0a7cc0;
    --sky:#0a95d4;
    --deep:#0c56a3;
    --panel:#eeeff1;
    --ink-grey:#58595b;
    --white:#ffffff;
    --line:#2b2b2b;
  }
  *{box-sizing:border-box;margin:0;padding:0}
  html,body{width:816px;height:1200px;overflow:hidden}
  body{background:var(--backdrop);font-family:"Montserrat",sans-serif;position:relative}
  .card{position:absolute;left:65.5px;width:685px;height:495px;background:var(--white);overflow:hidden}
  .card--front{top:75px}
  .card--back{top:618px;height:496px}
  .card__art{position:absolute;inset:0;width:100%;height:100%}
  .abs{position:absolute}

  /* front */
  .brand-mark{border:2.5px solid var(--white);border-radius:50%}
  .hex-brand__mark{left:158px;top:174px;width:66px;height:66px}
  .hex-brand__name{left:92px;width:200px;top:248px;text-align:center;color:var(--white);font-weight:500;font-size:31px;letter-spacing:1px;line-height:1}
  .hex-brand__sub{left:92px;width:200px;top:281px;text-align:center;color:var(--white);font-weight:400;font-size:12.5px;letter-spacing:.3px}
  .headline{left:64px;top:354px;line-height:36px;text-transform:uppercase}
  .headline__light{font-weight:300;font-size:31px;color:var(--navy);letter-spacing:-.3px}
  .headline__light .muted{color:var(--ink-grey)}
  .headline__bold{font-weight:900;font-size:31px;color:var(--navy);letter-spacing:.2px}
  .headline__bold .accent{color:var(--azure)}

  .offer{left:372px;top:170px;color:var(--white);text-transform:uppercase}
  .offer__lead{display:block;font-weight:300;font-size:16px;line-height:19px;letter-spacing:1px}
  .offer__figures{display:flex;align-items:baseline;gap:9px;line-height:48px}
  .offer__figure{font-weight:800;font-size:42px;letter-spacing:-.5px}
  .offer__or{font-weight:300;font-size:16px;letter-spacing:1px}
  .offer__tail{display:block;font-weight:300;font-size:17px;line-height:21px;letter-spacing:.2px;margin-top:2px}

  /* back */
  .mini-brand__mark{left:27px;top:29px;width:34px;height:34px;border-width:1.8px}
  .mini-brand__name{left:70px;top:31px;color:var(--white);font-weight:500;font-size:17px;letter-spacing:.5px;line-height:1;border-left:1px solid var(--white);padding-left:4px}
  .mini-brand__sub{left:71px;top:50px;color:var(--white);font-size:6.6px;letter-spacing:.2px;padding-left:4px}
  .intro{left:33px;top:118px;width:300px;color:var(--azure);font-weight:900;font-size:13.6px;line-height:17.3px;letter-spacing:.25px}
  .option-tag{display:inline-block;background:var(--azure);color:var(--white);font-weight:800;font-size:9.5px;letter-spacing:1px;text-transform:uppercase;padding:2px 8px;border-radius:3px;line-height:12px}
  .option-tag--one{left:33px;top:194px}
  .option-tag--two{left:33px;top:253px}
  .option-one{left:33px;top:212px;width:330px;color:var(--navy);font-weight:500;font-size:14.2px;line-height:17.6px}
  .option-two{left:35px;top:271px;width:262px;color:var(--navy);font-weight:500;font-size:11px;line-height:16.7px}
  .perks{left:45px;top:344px;list-style:none;color:var(--navy);font-size:9px;font-weight:500}
  .perks li{height:21px;padding-left:12px;position:relative}
  .perks li::before{content:"";position:absolute;left:0;top:4px;width:4.5px;height:4.5px;border-radius:50%;background:var(--azure)}
  .phone{left:36px;top:440px;display:flex;align-items:center;gap:8px;color:var(--navy);font-weight:500;font-size:24.5px;letter-spacing:.5px}
  .contact{left:250px;top:442px;color:var(--navy);font-size:7.2px;line-height:11px}
  .contact div{display:flex;align-items:center;gap:6px}
  .stamp{left:565px;top:42px;width:84px;height:84px;border:1.2px solid var(--line)}
  .address-line{left:418px;width:230px;height:0;border-top:1px solid var(--line)}
  .foot-brand__mark{left:547px;top:438px;width:33px;height:33px;border:1.8px solid var(--navy);border-radius:50%}
  .foot-brand__name{left:584px;top:441px;color:var(--navy);font-weight:500;font-size:16.5px;letter-spacing:.5px;line-height:1;border-left:1px solid var(--navy);padding-left:5px}
  .foot-brand__sub{left:584px;top:459px;color:var(--ink-grey);font-size:6.6px;letter-spacing:.2px;padding-left:6px}
</style>
</head>
<body>

<section class="card card--front" aria-label="Postcard front">
  <svg class="card__art" viewBox="0 0 1088 787" preserveAspectRatio="none">
    <defs>
      <linearGradient id="photoTone" x1="0" y1="0" x2="0.6" y2="1">
        <stop offset="0" stop-color="#d9e4ee"/>
        <stop offset=".45" stop-color="#c8c9c6"/>
        <stop offset="1" stop-color="#8d8478"/>
      </linearGradient>
      <linearGradient id="stripeTone" x1="0" y1="0" x2="1" y2="0">
        <stop offset="0" stop-color="#0a95d4"/>
        <stop offset="1" stop-color="#0c56a3"/>
      </linearGradient>
    </defs>
    <rect width="1088" height="787" fill="url(#photoTone)" role="img" aria-label="Photo of a modern two-storey white house with a dark tiled roof against a cloudy sky"/>
    <polygon points="0,600 985,0 1088,0 1088,787 0,787" fill="#ffffff"/>
    <polygon points="1014,0 1088,0 1088,760 470,395 470,330" fill="#1b4594"/>
    <polygon points="470,410 1088,772 1088,787 946,787 470,492" fill="url(#stripeTone)"/>
    <polygon points="305,195 473,291 473,474 305,570 137,474 137,291" fill="#ffffff"/>
    <polygon points="305,209 459,296 459,469 305,556 151,469 151,296" fill="#1b4594"/>
  </svg>
  <div class="abs brand-mark hex-brand__mark" aria-hidden="true"></div>
  <div class="abs hex-brand__name">HALDEN</div>
  <div class="abs hex-brand__sub">REAL ESTATE GROUP</div>

  <div class="abs offer">
    <span class="offer__lead">Get</span>
    <div class="offer__figures">
      <span class="offer__figure">110%</span>
      <span class="offer__or">or</span>
      <span class="offer__figure">160%</span>
    </div>
    <span class="offer__tail">of market value<br>for your property</span>
  </div>

  <h1 class="abs headline">
    <span class="headline__light">Monthly <span class="muted">Income</span></span><br>
    <span class="headline__bold">Without <span class="accent">Tenant<br>Headaches</span></span>
  </h1>
</section>

<section class="card card--back" aria-label="Postcard back">
  <svg class="card__art" viewBox="0 0 1088 788" preserveAspectRatio="none">
    <defs>
      <linearGradient id="cornerTone" x1="0" y1="0" x2="1" y2="0">
        <stop offset="0" stop-color="#0a95d4"/>
        <stop offset="1" stop-color="#0c6db5"/>
      </linearGradient>
    </defs>
    <rect width="633" height="788" fill="#eeeff1"/>
    <polygon points="0,0 270,0 270,98 104,190 0,126" fill="#ffffff"/>
    <polygon points="0,0 257,0 257,88 104,176 0,112" fill="#1b4594"/>
    <polygon points="258,0 633,0 633,286 258,76" fill="#ffffff"/>
    <polygon points="270,0 633,0 633,272 270,62" fill="url(#cornerTone)"/>
  </svg>

  <div class="abs brand-mark mini-brand__mark" aria-hidden="true"></div>
  <div class="abs mini-brand__name">HALDEN</div>
  <div class="abs mini-brand__sub">REAL ESTATE GROUP</div>

  <p class="abs intro">I am a new investor without down payment capital who still want to double our portfolio this year to grow our portfolio</p>

  <span class="abs option-tag option-tag--one">Option 1</span>
  <p class="abs option-one">you can receive 80% now cash and 30% over a short period of time including interest.</p>

  <span class="abs option-tag option-tag--two">Option 2</span>
  <p class="abs option-two">where act like a bank allowing you to make 150% if you finance the whole property(ies). No gimmicks and surprises, just simple unconventional financing.</p>

  <ul class="abs perks">
    <li>Formal protection as a lien holder against home</li>
    <li>No commission or closing cost</li>
    <li>Fast closings possible</li>
    <li>Property taken as is so no repairs.</li>
  </ul>

  <div class="abs phone">
    <svg width="23" height="23" viewBox="0 0 24 24" aria-hidden="true">
      <circle cx="12" cy="12" r="12" fill="var(--navy)"/>
      <path d="M8.2 5.8l2 2.3c.3.4.3.9 0 1.2l-1 1c.7 1.6 2 2.9 3.6 3.6l1-1c.3-.3.8-.3 1.2 0l2.3 2c.4.3.4.9 0 1.3l-1.2 1.2c-.6.6-1.5.7-2.3.4-3.2-1.3-5.6-3.7-6.9-6.9-.3-.8-.2-1.7.4-2.3l1.2-1.2c.4-.3 1-.3 1.300.1z" fill="#fff"/>
    </svg>
    <span>(123) 456 789</span>
  </div>
  <div class="abs contact">
    <div><svg width="9" height="9" viewBox="0 0 10 10" aria-hidden="true"><circle cx="5" cy="5" r="4.3" fill="none" stroke="var(--navy)" stroke-width="1"/><ellipse cx="5" cy="5" rx="1.9" ry="4.3" fill="none" stroke="var(--navy)" stroke-width=".8"/><line x1=".7" y1="5" x2="9.3" y2="5" stroke="var(--navy)" stroke-width=".8"/></svg>your website.com</div>
    <div><svg width="9" height="9" viewBox="0 0 10 10" aria-hidden="true"><rect x=".5" y="2" width="9" height="6.4" fill="none" stroke="var(--navy)" stroke-width="1"/><polyline points=".5,2 5,5.8 9.5,2" fill="none" stroke="var(--navy)" stroke-width="1"/></svg>hello@haldenmail.com</div>
  </div>

  <div class="abs stamp" aria-label="Stamp area"></div>
  <div class="abs address-line" style="top:176px"></div>
  <div class="abs address-line" style="top:256px"></div>
  <div class="abs address-line" style="top:337px"></div>

  <div class="abs foot-brand__mark" aria-hidden="true"></div>
  <div class="abs foot-brand__name">HALDEN</div>
  <div class="abs foot-brand__sub">REAL ESTATE GROUP</div>
</section>

</body>
</html>
```